fully distributed
Project: fully distributed
fully distributed  - Information Technology
Creative Brief
Use specific fonts
calibri
Simple
Doug Pelliver
CMO
482 Corwin St , Floor 6 New York NY 10019
doug.pelliver@tulvaro.com
logo only
marcste marcste
on 18 and 19 can you fade the grey a litle so it just looks like a faint color
Xpert Xpert
Sure Sir.
we like some of yr designs can u try the design of 17 with the physical layout of card 2
like what you have started will check each one out
thanks we are looking for stationary too
please add fax number 1 800 937 2584

```html
<!DOCTYPE html>
<html lang="en">
<head>
<meta charset="utf-8">
<title>Tulvaro Business Card</title>
<link href="https://fonts.googleapis.com/css2?family=Carlito:wght@400;700&display=swap" rel="stylesheet">
<style>
  :root {
    --page-bg: #e9e7e4;
    --card-white: #ffffff;
    --card-shade: #eeeeee;
    --panel-dark: #232323;
    --panel-edge: #cfcfcf;
    --accent-red: #e8343c;
    --ink-dark: #2b2b2b;
    --ink-soft: #6a6a6a;
    --ink-light: #f2f2f2;
  }
  html, body {
    margin: 0;
    width: 1200px;
    height: 901px;
    overflow: hidden;
    background: var(--page-bg);
    font-family: "Carlito", "Calibri", sans-serif;
  }
  .business-card {
    position: absolute;
    left: 150px;
    top: 193px;
    width: 900px;
    height: 514px;
    border-radius: 34px;
    overflow: hidden;
    background: linear-gradient(135deg, var(--card-white) 0%, var(--card-shade) 100%);
    box-shadow: 0 10px 30px rgba(0,0,0,0.18);
  }
  .card-shapes {
    position: absolute;
    inset: 0;
  }
  .brand-block {
    position: absolute;
    left: 70px;
    top: 178px;
  }
  .brand-name {
    font-size: 68px;
    font-weight: 400;
    color: var(--ink-dark);
    line-height: 1;
  }
  .brand-tagline {
    margin-top: 8px;
    font-size: 17px;
    font-weight: 400;
    color: var(--ink-soft);
    padding-left: 3px;
  }
  .person {
    position: absolute;
    left: 74px;
    top: 350px;
  }
  .person-name {
    font-size: 31px;
    font-weight: 400;
    letter-spacing: 1px;
    text-transform: uppercase;
    color: var(--ink-dark);
  }
  .person-title {
    font-size: 22px;
    color: var(--ink-dark);
    margin-top: 2px;
  }
  .contact-list {
    position: absolute;
    right: 46px;
    top: 48px;
    margin: 0;
    padding: 0;
    list-style: none;
    text-align: right;
    color: var(--ink-light);
    font-size: 19px;
  }
  .contact-list li {
    display: flex;
    justify-content: flex-end;
    align-items: center;
    gap: 12px;
    margin-bottom: 14px;
  }
  .contact-address {
    margin-bottom: 34px !important;
    line-height: 1.3;
    font-size: 21px;
  }
  .contact-icon {
    width: 18px;
    height: 18px;
    flex: none;
  }
</style>
</head>
<body>
  <div class="business-card">
    <svg class="card-shapes" viewBox="0 0 900 514" preserveAspectRatio="none" aria-hidden="true">
      <path d="M540,0 C470,140 450,330 330,514 L356,514 C478,335 500,150 575,0 Z" fill="var(--accent-red)"/>
      <path d="M590,0 C520,130 500,330 380,514 L900,514 L900,0 Z" fill="var(--panel-edge)"/>
      <path d="M600,0 C530,130 512,330 394,514 L900,514 L900,0 Z" fill="var(--panel-dark)"/>
    </svg>

    <div class="brand-block">
      <div class="brand-name">tulvaro</div>
      <div class="brand-tagline">The Fully Distributed Solution</div>
    </div>

    <div class="person">
      <div class="person-name">Doug Pelliver</div>
      <div class="person-title">CMO</div>
    </div>

    <ul class="contact-list">
      <li class="contact-address">482 Corwin St , Floor 6<br>New York NY 10019</li>
      <li>1 800 937 2584
        <svg class="contact-icon" viewBox="0 0 24 24"><path fill="currentColor" d="M6.6 10.8a15 15 0 0 0 6.6 6.6l2.2-2.2a1 1 0 0 1 1-.25 11.4 11.4 0 0 0 3.6.57 1 1 0 0 1 1 1V20a1 1 0 0 1-1 1A17 17 0 0 1 3 4a1 1 0 0 1 1-1h3.5a1 1 0 0 1 1 1c0 1.25.2 2.45.57 3.6a1 1 0 0 1-.25 1Z"/></svg>
      </li>
      <li>1 800 937 2584
        <svg class="contact-icon" viewBox="0 0 24 24"><rect x="6" y="2" width="12" height="20" rx="2" fill="none" stroke="currentColor" stroke-width="2"/><circle cx="12" cy="18" r="1.3" fill="currentColor"/></svg>
      </li>
      <li>1 800 937 2584
        <svg class="contact-icon" viewBox="0 0 24 24"><rect x="7" y="2" width="10" height="6" fill="none" stroke="currentColor" stroke-width="2"/><rect x="3" y="8" width="18" height="10" rx="1.5" fill="currentColor"/><rect x="7" y="15" width="10" height="7" fill="var(--panel-dark)" stroke="currentColor" stroke-width="2"/></svg>
      </li>
      <li>doug.pelliver@tulvaro.com
        <svg class="contact-icon" viewBox="0 0 24 24"><rect x="2" y="5" width="20" height="14" rx="2" fill="none" stroke="currentColor" stroke-width="2"/><path d="M3 6l9 7 9-7" fill="none" stroke="currentColor" stroke-width="2"/></svg>
      </li>
      <li>www.tulvaro.com
        <svg class="contact-icon" viewBox="0 0 24 24"><circle cx="12" cy="12" r="9.5" fill="none" stroke="currentColor" stroke-width="2"/><ellipse cx="12" cy="12" rx="4.5" ry="9.5" fill="none" stroke="currentColor" stroke-width="1.6"/><path d="M2.5 12h19" stroke="currentColor" stroke-width="1.6"/></svg>
      </li>
    </ul>
  </div>
</body>
</html>
```